Permanent Makeup Certificate for Lash Craft Institute Certified Artists

I need a beautifully designed certificate for my students who have successfully obtained my certification for Eyebrow Micropigmentation.

I have attached my sample certificate in InDesign format. This certificate is how I want the Certified Artist Certificate to read. My wording is extremely important for US Insurance reasons. I would like it to be in 11 x 17 inch format for USA printing.

I have also attached samples of certificates from other companies to give you an idea of how fancy I would like it to be. My company colors are pink and white, so I would like the dominant colors to be shades of pink and white. I like pink pastel combines with darker shades of pink and white. If the design calls for another color in addition to pink, that would also be great. I really like the colors in the Veluna Certificate.

I have attached a copy of my signature in .png

Target Market(s)

Beauty Industry

Industry/Entity Type

Artists

Font styles to use
Serif
Script

Colors
ffffff
f9d9e8
9bcb3c
cadf82
e667a6
e34297
eea4c8
b7a5cd

Requirements
Must have
• Wording exactly as I uploaded in InDesign file
Nice to have
• Beautiful images of female face, I am not sure if I like this idea. Just an experiement

```html
<!DOCTYPE html>
<html lang="en">
<head>
<meta charset="utf-8">
<title>Certificate of Excellence – Lash Craft Institute</title>
<link rel="stylesheet" href="https://fonts.googleapis.com/css2?family=Great+Vibes&family=Open+Sans:wght@400;600&family=Tinos&display=swap">
<style>
  :root {
    --paper: #ffffff;
    --ink: #1c1c1c;
    --muted: #4a4a4a;
    --accent: #b83b97;
    --accent-soft: #e7b6d6;
    --ornament: #f2dbea;
  }
  * { margin: 0; padding: 0; box-sizing: border-box; }
  html, body { width: 1200px; height: 800px; overflow: hidden; background: var(--paper); }
  .certificate { position: relative; width: 1200px; height: 800px; background: var(--paper); color: var(--ink); }
  .abs { position: absolute; }
  .corner { width: 112px; height: 112px; background: var(--ornament); border-radius: 6px; }
  .corner--tl { left: 35px; top: 40px; }
  .corner--tr { right: 35px; top: 40px; }
  .corner--bl { left: 35px; bottom: 40px; }
  .corner--br { right: 35px; bottom: 40px; }
  .side-rule { top: 245px; width: 7px; height: 310px; border-left: 2px solid var(--accent); border-right: 2px solid var(--accent); }
  .side-rule--left { left: 35px; }
  .side-rule--right { right: 35px; }
  .brand { left: 0; right: 0; top: 128px; text-align: center; font-family: "Open Sans", sans-serif; font-weight: 600; font-size: 30px; color: var(--accent); letter-spacing: 1px; }
  .title { left: 0; right: 0; top: 205px; text-align: center; font-family: "Great Vibes", cursive; font-size: 72px; line-height: 1; color: var(--ink); }
  .presented { left: 0; right: 0; top: 298px; text-align: center; font-family: "Open Sans", sans-serif; font-size: 21px; color: var(--muted); }
  .presented-rule { left: 296px; top: 318px; }
  .recipient { left: 0; right: 0; top: 378px; text-align: center; font-family: "Great Vibes", cursive; font-size: 54px; line-height: 1; }
  .name-rule { left: 369px; top: 443px; width: 459px; height: 8px; border-top: 2px solid var(--accent); border-bottom: 2px solid var(--accent); }
  .statement { left: 0; right: 0; top: 466px; text-align: center; font-family: "Tinos", serif; font-size: 17px; line-height: 22px; color: var(--ink); }
  .seal { left: 550px; top: 555px; }
  .date-block, .signature-block { text-align: center; font-family: "Open Sans", sans-serif; }
  .date-block { left: 227px; top: 630px; width: 180px; }
  .signature-block { left: 776px; top: 615px; width: 196px; }
  .date-value { font-size: 15px; color: var(--ink); padding-bottom: 3px; border-bottom: 2px solid var(--accent); }
  .label { font-size: 17px; font-weight: 600; margin-top: 5px; }
  .signature-mark { height: 36px; margin: 0 10px 4px; background: var(--ornament); border-bottom: 2px solid var(--accent); }
  .role { font-size: 14px; color: var(--muted); line-height: 20px; margin-top: 4px; }
  .divider { left: 510px; top: 727px; }
</style>
</head>
<body>
<main class="certificate">
  <div class="abs corner corner--tl" role="img" aria-label="Decorative pink flourish corner ornament"></div>
  <div class="abs corner corner--tr" role="img" aria-label="Decorative pink flourish corner ornament"></div>
  <div class="abs corner corner--bl" role="img" aria-label="Decorative pink flourish corner ornament"></div>
  <div class="abs corner corner--br" role="img" aria-label="Decorative pink flourish corner ornament"></div>

  <div class="abs side-rule side-rule--left"></div>
  <div class="abs side-rule side-rule--right"></div>

  <div class="abs brand">Lash Craft Institute</div>

  <h1 class="abs title">Certificate of Excellence</h1>
  <p class="abs presented">This certificate is proudly presented to</p>
  <svg class="abs presented-rule" width="608" height="24" viewBox="0 0 608 24">
    <circle cx="10" cy="12" r="5" fill="none" stroke="var(--accent)" stroke-width="2"/>
    <line x1="16" y1="14" x2="592" y2="14" stroke="var(--accent)" stroke-width="2"/>
    <circle cx="598" cy="12" r="5" fill="none" stroke="var(--accent)" stroke-width="2"/>
  </svg>

  <p class="abs recipient">First &amp; Last Name</p>
  <div class="abs name-rule"></div>

  <p class="abs statement">
    Has successfully proven to be an<br>
    Artist of the Highest Standard in Eyebrow Micropigmentation<br>
    using the LASH CRAFT INTERNATIONAL® Microblading Method
  </p>

  <svg class="abs seal" width="100" height="140" viewBox="0 0 100 140">
    <path d="M32 70 L32 134 L50 120 L68 134 L68 70 Z" fill="var(--accent)"/>
    <circle cx="50" cy="52" r="48" fill="var(--accent)"/>
    <circle cx="50" cy="52" r="34" fill="none" stroke="var(--paper)" stroke-width="2"/>
  </svg>

  <div class="abs date-block">
    <div class="date-value">22.07.2017</div>
    <div class="label">DATE</div>
  </div>

  <div class="abs signature-block">
    <div class="signature-mark" role="img" aria-label="Handwritten signature of the master instructor"></div>
    <div class="label">CLARA RUTH VESPER</div>
    <div class="role">Master Instructor<br>Lash Craft International</div>
  </div>

  <svg class="abs divider" width="180" height="18" viewBox="0 0 180 18">
    <g fill="var(--accent)">
      <rect x="2" y="5" width="7" height="7" transform="rotate(45 5.5 8.5)"/>
      <rect x="86" y="1" width="7" height="7" transform="rotate(45 89.5 4.5)"/>
      <rect x="86" y="10" width="7" height="7" transform="rotate(45 89.5 13.5)"/>
      <rect x="171" y="5" width="7" height="7" transform="rotate(45 174.5 8.5)"/>
    </g>
    <line x1="10" y1="9" x2="76" y2="9" stroke="var(--accent)" stroke-width="1.5"/>
    <line x1="104" y1="9" x2="170" y2="9" stroke="var(--accent)" stroke-width="1.5"/>
  </svg>
</main>
</body>
</html>
```